Brackenfield Prime Healthcare Needs a Business Card Design

We need a business card design for a company based in Shorewood IL called "Brackenfield Prime Healthcare". We provide an integrated medical model involving chiropractic, trigger point injections and other medical services in one location. I have attached our logo to this with the colors being in the puzzle design of the logo. We are looking for a great design that will WOW those around us but also be able to communicate our information easily

Industry/Entity Type

Medical

Contact Information for Business Card

This is a integrated Medical office featuring numerous services to clients in the office.

Requirements
Must have
• Logo

```html
<!DOCTYPE html>
<html lang="en">
<head>
<meta charset="utf-8">
<title>Brackenfield Prime Healthcare – Business Card</title>
<link rel="stylesheet" href="https://fonts.googleapis.com/css2?family=Jost:wght@400&family=Tinos&display=swap">
<style>
  :root {
    --page: #ffffff;
    --teal-deep: #12353a;
    --teal-mid: #2a7479;
    --teal-light: #3a9ea2;
    --green-deep: #2a3a0c;
    --green-mid: #5f8526;
    --green-light: #7ca83a;
    --brand-blue: #3a78b8;
    --frame-blue: #9cc3e0;
    --ink-light: #ffffff;
  }
  * { margin: 0; padding: 0; box-sizing: border-box; }
  html, body { width: 1200px; height: 1000px; overflow: hidden; background: var(--page); }
  .canvas { position: relative; width: 1200px; height: 1000px; }

  .card {
    position: absolute; left: 183px; width: 840px; height: 479px; overflow: hidden;
    background: linear-gradient(90deg, var(--teal-deep) 0%, var(--teal-mid) 22%, var(--teal-light) 50%, var(--teal-mid) 80%, var(--teal-deep) 100%);
  }
  .card--front { top: 16px; }
  .card--back { top: 511px; }

  .band-horizontal {
    position: absolute; left: 0; width: 100%;
    background: linear-gradient(90deg, var(--green-deep) 0%, var(--green-mid) 30%, var(--green-light) 55%, var(--green-mid) 80%, var(--green-deep) 100%);
  }
  .card--front .band-horizontal { top: 406px; height: 73px; }
  .card--back .band-horizontal { top: 258px; height: 64px; }

  .band-vertical {
    position: absolute; top: 0;
    background: linear-gradient(180deg, var(--green-deep) 0%, var(--green-mid) 25%, var(--green-light) 50%, var(--green-mid) 80%, var(--green-deep) 100%);
  }
  .band-vertical--thin { left: 722px; width: 22px; height: 406px; }
  .band-vertical--wide { left: 757px; width: 65px; height: 479px; }

  .brand-plate {
    position: absolute; left: 0; width: 390px; height: 89px; background: #fff;
  }
  .card--front .brand-plate { top: 0; }
  .card--back .brand-plate { top: 167px; }
  .brand-plate__frame {
    position: absolute; left: 6px; top: 6px; right: 6px; bottom: 6px;
    border: 1px solid var(--frame-blue);
    display: flex; align-items: center; gap: 10px; padding-left: 7px;
  }
  .brand-plate__mark { width: 62px; height: 62px; background: var(--brand-blue); flex: none; }
  .brand-plate__name {
    font-family: "Jost", sans-serif; font-weight: 400; font-size: 24px; line-height: 30px;
    color: var(--brand-blue); letter-spacing: 0.5px;
  }

  .contact {
    position: absolute; right: 120px; text-align: right; color: var(--ink-light);
    font-family: "Jost", sans-serif; font-size: 24px; line-height: 24px;
  }
  .contact__name {
    font-family: "Tinos", "Times New Roman", serif; font-size: 46px; line-height: 46px;
    font-weight: 400; margin-bottom: 4px;
  }
  .contact--identity { top: 102px; }
  .contact--details { top: 275px; }
</style>
</head>
<body>
<div class="canvas">
  <section class="card card--front">
    <div class="band-vertical band-vertical--thin"></div>
    <div class="band-horizontal"></div>
    <div class="band-vertical band-vertical--wide"></div>

    <div class="brand-plate">
      <div class="brand-plate__frame">
        <div class="brand-plate__mark"></div>
        <div class="brand-plate__name">BRACKENFIELD PRIME<br>HEALTHCARE</div>
      </div>
    </div>

    <div class="contact contact--identity">
      <h1 class="contact__name">Full Name</h1>
      <p>Job title</p>
      <p>email other</p>
    </div>
    <div class="contact contact--details">
      <p>address 1</p>
      <p>address 2</p>
      <p>phone other</p>
      <p>fax other</p>
      <p>webs other</p>
    </div>
  </section>

  <section class="card card--back">
    <div class="band-horizontal"></div>
    <div class="brand-plate">
      <div class="brand-plate__frame">
        <div class="brand-plate__mark"></div>
        <div class="brand-plate__name">BRACKENFIELD PRIME<br>HEALTHCARE</div>
      </div>
    </div>
  </section>
</div>
</body>
</html>
```